Personalized Technology Company Needs a Business Card

I need a double-sided business card. Both sides will have the logo, and the contact information. One side will be black, with the white / gray logo, and the other will be white, with the black / gray logo. The black side will have the text "Custom Gaming PC's" and will have a water-cooled gaming PC image. The white side will have the text "Custom Business Computers & Consulting", and will have a business / enterprise PC image. Feel free to add a conservative image in the background, while the color remains unchanged. I'm uploading the base logo (transparent), so you can modify the colors, both the finished colored logos and an idea of ​​the business card (with the current information, just missing the website, which is www.volinexsystems.com, please add it.) Thank you so much for your effort, I'll be specting your cool designs. Good Luck!

Target Market(s)

Gamers & Entrepreneurs / Business Owners / Chief Technology Officers

Industry/Entity Type

Technology Equipment

Contact Information for Business Card

I need a double-sided business card. Both sides will have the logo, and the contact information. One side will be black, with the white/gray logo, and the other one will be white, with the black/gray logo. The black side will have the text "Custom Gaming PC's" and will have a water-cooled gaming PC image. The white side will have the text "Custom Business Computers & Consulting", and will have a business/enterprise PC image. Feel free to add a conservative image in the background, whilst the color remains unchanged.

I'm uploading the base logo (transparent), so you can modify the colors, both the finished colored logos and an idea of the business card (with the actual information, just missing the website, which is www.volinexsystems.com, please add it.)

Thank you so much for your effort, I'll be specting your cool designs. Good Luck!

Font styles to use
Serif

Colors
000000
757575
ffffff

Requirements
Must have
• Please See Description
Nice to have
• Please See Description
Should not have
• Please See Description

```html
<!DOCTYPE html>
<html lang="en">
<head>
<meta charset="utf-8">
<title>Volinex Systems – Business Card</title>
<link rel="stylesheet" href="https://fonts.googleapis.com/css2?family=Michroma&family=Poppins:wght@300;400;600&display=swap">
<style>
  :root {
    --stage: #b3b2aa;
    --ink: #000000;
    --grey: #757575;
    --paper: #ffffff;
    --accent: #2549e3;
    --night-top: #0e2236;
    --night-bottom: #04070c;
    --mist-a: #fbfbfb;
    --mist-b: #e6e6e6;
    --rule: #3a3a3a;
  }
  * { box-sizing: border-box; margin: 0; padding: 0; }
  html, body {
    width: 1200px;
    height: 900px;
    overflow: hidden;
    background: var(--stage);
  }
  .card {
    position: absolute;
    top: 298px;
    width: 504px;
    height: 304px;
    border-radius: 22px;
    overflow: hidden;
  }
  .card--gaming { left: 73px; }
  .card--business { left: 640px; }

  .card__backdrop {
    position: absolute;
    inset: 0;
  }
  .card--gaming .card__backdrop {
    background:
      radial-gradient(ellipse at 30% 75%, rgba(40, 90, 150, 0.45), transparent 60%),
      radial-gradient(ellipse at 85% 60%, rgba(120, 50, 40, 0.35), transparent 55%),
      linear-gradient(160deg, var(--night-top), var(--night-bottom));
  }
  .card--business .card__backdrop {
    background:
      radial-gradient(ellipse at 78% 40%, var(--mist-b), transparent 65%),
      linear-gradient(180deg, var(--mist-a), #f1f1f1);
  }

  .brand-name {
    position: absolute;
    font-family: "Poppins", sans-serif;
    font-weight: 600;
    letter-spacing: 4px;
    white-space: nowrap;
  }
  .card--gaming .brand-name {
    top: 138px;
    left: 0;
    width: 100%;
    text-align: center;
    font-size: 30px;
    color: var(--paper);
  }
  .card--business .brand-name {
    top: 104px;
    right: 32px;
    font-size: 30px;
    color: var(--ink);
  }

  .tagline--gaming {
    position: absolute;
    top: 238px;
    left: 0;
    width: 100%;
    text-align: center;
    font-family: "Michroma", sans-serif;
    font-size: 23px;
    letter-spacing: 3px;
    color: var(--paper);
  }
  .tagline--gaming .highlight { color: var(--accent); }

  .tagline--business {
    position: absolute;
    top: 196px;
    right: 32px;
    text-align: right;
    font-family: "Poppins", sans-serif;
    font-weight: 300;
    font-size: 19px;
    line-height: 28px;
    color: #222222;
    letter-spacing: 0.5px;
  }
  .tagline--business .highlight { color: var(--accent); font-weight: 400; }

  .contact-rule {
    position: absolute;
    top: 272px;
    left: 0;
    width: 258px;
    height: 1px;
    background: var(--rule);
  }
  .contact-web {
    position: absolute;
    top: 262px;
    right: 32px;
    display: flex;
    align-items: center;
    gap: 5px;
    font-family: "Poppins", sans-serif;
    font-size: 13px;
    color: #222222;
  }
  .contact-web svg { width: 10px; height: 10px; }
</style>
</head>
<body>

<section class="card card--gaming" aria-label="Gaming side of the business card">
  <div class="card__backdrop" role="img" aria-label="Dark photograph of a water-cooled gaming PC interior"></div>
  <div class="brand-name">VOLINEX SYSTEMS</div>
  <p class="tagline--gaming">CUSTOM <span class="highlight">GAMING</span> PC</p>
</section>

<section class="card card--business" aria-label="Business side of the business card">
  <div class="card__backdrop" role="img" aria-label="Faint photograph of a laptop computer"></div>
  <div class="brand-name">VOLINEX SYSTEMS</div>
  <p class="tagline--business">CUSTOM <span class="highlight">BUSINESS</span><br>COMPUTERS &amp; CONSULTING</p>
  <div class="contact-rule"></div>
  <p class="contact-web">www.volinexsystems.com
    <svg viewBox="0 0 10 10" aria-hidden="true">
      <circle cx="5" cy="5" r="4.3" fill="none" stroke="#555" stroke-width="0.9"/>
      <ellipse cx="5" cy="5" rx="1.9" ry="4.3" fill="none" stroke="#555" stroke-width="0.7"/>
      <line x1="0.7" y1="5" x2="9.3" y2="5" stroke="#555" stroke-width="0.7"/>
    </svg>
  </p>
</section>

</body>
</html>
```